A Pest Control Company needs a Door Hanger for targetting residential market

We need a door hanger design to target residential households in a campaign which will basically focus on controlling insect pests when they are coming out of hibernation in spring and early summer. We want to create awareness that controlling these insects like ants,wasps,box elder bugs etc at this stage will be nipping the evil in the bud before they become a nuisance.We will offer a home care plan involving exterior insect treatment and preventive treatment for mice inside the house.We will show them it will be economical to act before it becomes a problem.We will invite them to call us for a quote.

The design should be a call to action type, driving the customers to call us for more details ,pricing and action.
Updates

Reason: Still waiting for more designs. Thanks

Target Market(s)

Residential households(Single family dwellings)

Industry/Entity Type

Residential

Requirements
Must have
• Some pictures of the pests,home etc

```html
<!DOCTYPE html>
<html lang="en">
<head>
<meta charset="utf-8">
<title>Northfield Pest Control – Door Hanger</title>
<link rel="stylesheet" href="https://fonts.googleapis.com/css2?family=Arimo:ital,wght@1,700&family=Montserrat:wght@500&family=Open+Sans:wght@400;700&family=PT+Sans:wght@400&display=swap">
<style>
  :root {
    --blue-dark: #1c3f9c;
    --blue-light: #2a9ad8;
    --red: #e31b23;
    --yellow: #f7ea00;
    --white: #ffffff;
    --ink: #111111;
    --photo-warm: #b8743a;
    --photo-light: #f1ece6;
    --btn-top: #4f8fe8;
    --btn-bottom: #0a2d8a;
    --btn-rim: #c9ccd3;
  }
  * { margin: 0; padding: 0; box-sizing: border-box; }
  html, body { width: 1200px; height: 2933px; overflow: hidden; background: var(--white); }
  .hanger { position: relative; width: 1200px; height: 2933px; overflow: hidden; background: var(--white); }
  .hanger-top { position: absolute; inset: 0 0 auto 0; width: 1200px; height: 1240px; }
  .headline {
    position: absolute; left: 90px; top: 440px; width: 1120px;
    transform: rotate(-14deg); transform-origin: center;
    font-family: "Arimo", Arial, sans-serif; font-weight: 700; font-style: italic;
    font-size: 76px; line-height: 1.12; color: var(--yellow); text-align: center;
    text-shadow: 4px 4px 0 #3a0a0a, 6px 6px 8px rgba(0,0,0,.5);
  }
  .sleep-marks {
    position: absolute; left: 70px; top: 985px;
    font-family: "Arimo", Arial, sans-serif; font-weight: 700; font-size: 46px; color: var(--white);
  }
  .sleep-marks span { position: absolute; }
  .pest-photo {
    position: absolute; left: 0; top: 1000px; width: 1200px; height: 560px;
    background: radial-gradient(ellipse 55% 40% at 58% 55%, var(--photo-warm) 0%, #8a4a1e 45%, rgba(241,236,230,0) 75%);
  }
  .quote-button {
    position: absolute; left: 190px; top: 1600px; width: 817px; height: 160px;
    border-radius: 40px; border: 10px solid var(--btn-rim);
    background: linear-gradient(180deg, var(--btn-top) 0%, #1a53c4 48%, var(--btn-bottom) 52%, #1540a8 100%);
    box-shadow: 0 6px 14px rgba(0,0,0,.35);
    display: flex; align-items: center; justify-content: center;
    font-family: "PT Sans", "Trebuchet MS", sans-serif; font-size: 58px; color: var(--white);
  }
  .phone {
    position: absolute; left: 0; top: 1780px; width: 1200px; text-align: center;
    font-family: "Montserrat", Arial, sans-serif; font-weight: 500; font-size: 84px;
    letter-spacing: 6px; color: var(--ink);
  }
  .features {
    position: absolute; left: 0; top: 1925px; width: 1200px; list-style: none; text-align: center;
    font-family: "Open Sans", Arial, sans-serif; font-size: 41px; line-height: 73px; color: var(--ink);
  }
  .brand-mark {
    position: absolute; left: 0; top: 2600px; width: 1200px;
    display: flex; align-items: center; justify-content: center; gap: 28px;
  }
  .brand-mark .dot { width: 80px; height: 80px; border-radius: 50%; background: var(--red); }
  .brand-mark .name {
    font-family: "Open Sans", Arial, sans-serif; font-weight: 700; font-size: 78px;
    letter-spacing: 6px; color: var(--red);
  }
  .company-name {
    position: absolute; left: 0; top: 2795px; width: 1200px; text-align: center;
    font-family: "Open Sans", Arial, sans-serif; font-weight: 700; font-size: 72px; color: var(--red);
  }
</style>
</head>
<body>
<main class="hanger">
  <svg class="hanger-top" viewBox="0 0 1200 1240" aria-hidden="true">
    <defs>
      <linearGradient id="sky" x1="0" y1="0" x2="1" y2="0">
        <stop offset="0" stop-color="var(--blue-dark)"/>
        <stop offset="1" stop-color="var(--blue-light)"/>
      </linearGradient>
    </defs>
    <rect width="1200" height="560" fill="url(#sky)"/>
    <polygon points="0,525 1200,134 1200,807 489,1027 61,1222 220,1088 0,1149" fill="var(--red)"/>
    <line x1="599" y1="0" x2="599" y2="30" stroke="var(--white)" stroke-width="4"/>
    <circle cx="599" cy="134" r="115" fill="var(--white)"/>
  </svg>

  <div class="pest-photo" role="img" aria-label="Photo of a cockroach lying asleep on its back beside a green pillow"></div>

  <div class="sleep-marks" aria-hidden="true">
    <span style="left:80px;top:0">Z</span>
    <span style="left:115px;top:50px">Z</span>
    <span style="left:55px;top:100px">Z</span>
    <span style="left:10px;top:150px">Z</span>
  </div>

  <h1 class="headline">Pest Controled early<br>before they come out of<br>hibernation in Spring and<br>early Summer!</h1>

  <div class="quote-button">call us for a FREE quote</div>
  <div class="phone">1-800-555-0142</div>

  <ul class="features">
    <li>Govt. Licensed and Fully Insured</li>
    <li>Environmentally Friendly Techniques</li>
    <li>Pest Inspections using Fibro Optic &amp; Infrared Technology</li>
    <li>Open 7 days a week</li>
    <li>Written Guarantees</li>
    <li>15 % Seniors Discount</li>
    <li>WSIB Insured</li>
    <li>Government Contractors</li>
  </ul>

  <div class="brand-mark">
    <span class="dot"></span>
    <span class="name">NORTHFIELD</span>
  </div>
  <div class="company-name">Northfield Pest Control</div>
</main>
</body>
</html>
```